I am looking for a flyer design for my upcoming symposium. Here are the details for the flyer and pictures of speakers are attached.

Name of Symposium: Lattice and Pathway Biosciences Symposium, Sponsored by the Corvale Chromatin Institute and the Department of Bioengineering
Date: January 8, 2018
Location: Havergill Auditorium, Tarnby Center for Applied Discovery, 2175 Orchard Terrace Ave, Philadelphia, PA 19127

Reception to follow after the symposium.

Also, please add - Register and upload abstracts for the symposium at www.qzvmrk.com. Registration and abstract submission closes on January 4, 2018.

Keynote Speaker:
Marthe Quillon, Ph.D.
NTVO Director General; Professor, Lyceum of Norvane; Director, Genetics and Developmental Biology at Institut Bramoux
Lyceum of Norvane, NTVO, Institut Bramoux
"Title of talk TBA."

Speakers:
Lena Drewcott, Ph.D.
Assistant Professor of Cell and Developmental Biology
Halvering State University, HMCS
"Title of talk TBA."

Paul Marden, Ph.D.
Assistant Professor of Genetics
"Title of talk TBA."

Ilse Varga, Ph.D.
Professor, Ostrander University
Otto Wenzlau Center for Molecular Medicine
"Title of talk TBA."

Jun Hao, Ph.D.
Professor of Cellular and Molecular Medicine
Coastal Meridian University
"Title of talk TBA."

Wei Lun, Ph.D.
Associate Professor of Pediatrics
The Youth Medical Pavilion of Philadelphia
"Spatial genome re-organization between fetal and adult hematopoietic stem cells."

Mei Zhou, Ph.D.
Professor, Department of Genetics
Ellsworth Medical School
"Title of talk TBA."

```html
<!DOCTYPE html>
<html lang="en">
<head>
<meta charset="utf-8">
<title>Lattice and Pathway Biosciences Symposium</title>
<link rel="stylesheet" href="https://fonts.googleapis.com/css2?family=Montserrat:wght@300;400;700;800&family=Open+Sans:wght@400;600;700&display=swap">
<style>
  :root {
    --paper: #ffffff;
    --red-deep: #5a0a10;
    --red-mid: #a3111c;
    --red-bright: #d8202c;
    --panel-dark: #2c0b0e;
    --panel-mid: #4a1418;
    --yellow: #f5d53a;
    --sky: #8fd3ee;
    --white: #ffffff;
    --navy: #1d3a52;
    --ink: #33475a;
    --divider: #c8202c;
  }
  * { margin: 0; padding: 0; box-sizing: border-box; }
  html, body { width: 927px; height: 1200px; overflow: hidden; background: var(--paper); }
  body { position: relative; font-family: "Open Sans", Arial, sans-serif; }

  .hero {
    position: absolute; left: 12px; top: 12px; width: 903px; height: 940px;
    background: var(--panel-dark);
    box-shadow: 0 4px 6px rgba(0,0,0,0.25);
  }
  .hero-visual {
    position: absolute; left: 0; top: 0; width: 437px; height: 940px;
    background:
      radial-gradient(ellipse 55% 40% at 60% 62%, rgba(255,190,190,0.55), transparent 70%),
      linear-gradient(180deg, var(--red-deep) 0%, var(--red-mid) 45%, var(--red-bright) 70%, var(--red-deep) 100%);
  }
  .hero-right {
    position: absolute; left: 441px; top: 0; width: 462px; height: 940px;
    background: radial-gradient(ellipse 70% 60% at 30% 55%, var(--panel-mid), var(--panel-dark) 75%);
  }
  .hero-divider {
    position: absolute; left: 437px; top: 0; width: 4px; height: 940px; background: var(--divider);
  }

  .title {
    position: absolute; left: 12px; top: 46px; width: 437px; text-align: center;
    font-family: "Montserrat", Arial, sans-serif; line-height: 62px;
  }
  .title .strong { display: block; color: var(--yellow); font-weight: 800; font-size: 47px; letter-spacing: 0.5px; }
  .title .light { display: block; color: var(--white); font-weight: 400; font-size: 47px; letter-spacing: 1px; }
  .sponsor {
    position: absolute; left: 12px; top: 305px; width: 437px; text-align: center;
    color: var(--white); font-size: 16.5px; line-height: 22px;
  }

  .section-label {
    position: absolute; left: 612px; display: flex; align-items: center; gap: 8px;
    font-family: "Montserrat", Arial, sans-serif; font-weight: 700; font-size: 16px; width: 303px;
  }
  .section-label::after { content: ""; flex: 1; height: 2px; background: currentColor; }
  .label-keynote { top: 52px; color: var(--yellow); }
  .label-speakers { top: 251px; left: 609px; width: 306px; color: var(--sky); }

  .portrait {
    position: absolute; border-radius: 50%; border: 3px solid var(--white);
    background: radial-gradient(circle at 50% 40%, #c49a82 0%, #7a5646 55%, #3d2b24 100%);
  }
  .portrait-keynote { left: 489px; top: 95px; width: 112px; height: 112px; }
  .portrait-speaker { left: 506px; width: 88px; height: 88px; }

  .bio {
    position: absolute; left: 608px; width: 300px;
    color: var(--white); font-size: 12.5px; line-height: 16.2px;
  }
  .bio .name { display: block; font-weight: 700; font-size: 13px; color: var(--sky); }
  .bio-keynote { left: 609px; top: 109px; }
  .bio-keynote .name { color: var(--yellow); }

  .org-marks { position: absolute; left: 44px; top: 1014px; }
  .org-mark {
    display: flex; align-items: center; gap: 10px;
    font-family: "Open Sans", Arial, sans-serif; font-weight: 600; color: var(--navy);
  }
  .org-mark .dot { width: 30px; height: 30px; background: var(--navy); border-radius: 50%; }
  .org-mark-engineering { font-size: 20px; }
  .org-mark-institute { font-size: 15px; margin-top: 48px; }
  .org-mark-institute .dot { background: var(--red-bright); }

  .details { position: absolute; right: 35px; top: 990px; text-align: right; color: var(--ink); }
  .details .date {
    font-family: "Montserrat", Arial, sans-serif; font-weight: 700; font-size: 31px; color: var(--navy); line-height: 40px;
  }
  .details .venue { margin-top: 10px; font-size: 14.5px; line-height: 18px; }
  .details .register { margin-top: 22px; font-size: 16.5px; line-height: 21px; }
  .details .register strong { font-weight: 700; color: var(--navy); }
  .details .reception { margin-top: 12px; font-size: 16.5px; }
</style>
</head>
<body>
  <section class="hero">
    <div class="hero-visual" role="img" aria-label="Red-toned portrait overlaid with genome sequencing bands and binary digits"></div>
    <div class="hero-divider"></div>
    <div class="hero-right"></div>
  </section>

  <h1 class="title">
    <span class="strong">LATTICE AND</span>
    <span class="strong">PATHWAY</span>
    <span class="strong">BIOSCIENCES</span>
    <span class="light">SYMPOSIUM</span>
  </h1>
  <p class="sponsor">Sponsored by the Corvale Chromatin Institute<br>and the Department of Bioengineering</p>

  <div class="section-label label-keynote">Keynote Speaker</div>
  <div class="portrait portrait-keynote" role="img" aria-label="Photo of Marthe Quillon"></div>
  <p class="bio bio-keynote"><span class="name">Marthe Quillon, Ph.D.</span>NTVO Director General; Professor, Lyceum of Norvane; Director, Genetics and Developmental Biology at Institut Bramoux Lyceum of Norvane, NTVO, Institut Bramoux "Title of talk TBA."</p>

  <div class="section-label label-speakers">Speakers</div>

  <div class="portrait portrait-speaker" style="top:296px" role="img" aria-label="Photo of Lena Drewcott"></div>
  <p class="bio" style="top:303px"><span class="name">Lena Drewcott, Ph.D.</span>Assistant Professor of Cell and<br>Developmental Biology<br>Halvering State University, HMCS<br>"Title of talk TBA."</p>

  <div class="portrait portrait-speaker" style="top:401px" role="img" aria-label="Photo of Paul Marden"></div>
  <p class="bio" style="top:411px"><span class="name">Paul Marden, Ph.D.</span>Assistant Professor of Genetics<br>Halvering State University, HMCS<br>"Title of talk TBA."</p>

  <div class="portrait portrait-speaker" style="top:508px" role="img" aria-label="Photo of Ilse Varga"></div>
  <p class="bio" style="top:514px"><span class="name">Ilse Varga, Ph.D.</span>Professor, Ostrander University<br>Otto Wenzlau Center for<br>Molecular Medicine | "Title of talk TBA."</p>

  <div class="portrait portrait-speaker" style="top:613px" role="img" aria-label="Photo of Jun Hao"></div>
  <p class="bio" style="top:618px"><span class="name">Jun Hao, Ph.D.</span>Professor of Cellular and<br>Molecular Medicine<br>Coastal Meridian University<br>"Title of talk TBA."</p>

  <div class="portrait portrait-speaker" style="top:719px" role="img" aria-label="Photo of Wei Lun"></div>
  <p class="bio" style="top:729px"><span class="name">Wei Lun, Ph.D.</span>Associate Professor of Pediatrics<br>The Youth Medical Pavilion of Philadelphia<br>"Spatial genome re-organization<br>between fetal and adult<br>hematopoietic stem cells."</p>

  <div class="portrait portrait-speaker" style="top:826px" role="img" aria-label="Photo of Mei Zhou"></div>
  <p class="bio" style="top:868px"><span class="name">Mei Zhou, Ph.D.</span>Professor, Department of Genetics<br>Ellsworth Medical School | "Title of talk TBA."</p>

  <div class="org-marks">
    <div class="org-mark org-mark-engineering"><span class="dot"></span>Halvering Engineering</div>
    <div class="org-mark org-mark-institute"><span class="dot"></span>Corvale Chromatin Institute</div>
  </div>

  <div class="details">
    <p class="date">January 8, 2018</p>
    <p class="venue">Havergill Auditorium, Tarnby Center for Applied Discovery,<br>2175 Orchard Terrace Ave, Philadelphia, PA 19127</p>
    <p class="register">Register and upload abstracts for the symposium at www.qzvmrk.com.<br>Registration and abstract submission closes on <strong>January 4, 2018.</strong></p>
    <p class="reception">Reception to follow after the symposium.</p>
  </div>
</body>
</html>
```